【依頼の目的/概要】
電子書籍(lumora)の表紙デザインをお願いします。

【画像サイズ】 ※RZBより抜粋
表紙ファイルの理想的な寸法 2,560×1,600ピクセルです。
注:画像の寸法は 1,000×625ピクセル以上であることが必要です。
画像の最大の寸法は 10,000×10,000ピクセルです。

【タイトル】

5つの航路・ヴォルテノ大年譜など
人類普遍の必読真理書をギュっと1冊にまとめました

【著者】

RUNO

【本の内容】

5つの航路・ヴォルテノ大年譜などの人間心理・成功本を
まとめて解説した本です。

※本文を参考資料として添付します。

【デザイン要望】

特にイメージにこだわりはありませんので、
自由な発送でのデザインご応募を楽しみにしています。

※次点の方への参加報酬を設定致しました。

※その他 必要な情報がありましたら、お問い合わせください。

```html
<!DOCTYPE html>
<html lang="ja">
<head>
<meta charset="utf-8">
<title>5つの航路・ヴォルテノ大年譜など 人類普遍の必読真理書をギュっと1冊にまとめました</title>
<link rel="stylesheet" href="https://fonts.googleapis.com/css2?family=M+PLUS+Rounded+1c:wght@500;800;900&display=swap">
<style>
  :root {
    --ground: #e4d46b;
    --band: #f07191;
    --sky: #6fd3ea;
    --ink: #24519a;
    --rose: #e9567e;
  }
  * { margin: 0; padding: 0; box-sizing: border-box; }
  html, body { width: 750px; height: 1200px; overflow: hidden; }
  body {
    background: var(--ground);
    font-family: "M PLUS Rounded 1c", sans-serif;
    position: relative;
  }
  .cover { position: absolute; inset: 0; }
  .title-line {
    position: absolute;
    display: flex;
    align-items: center;
    white-space: nowrap;
    overflow: hidden;
    background: var(--band);
    color: var(--sky);
    font-weight: 900;
    -webkit-text-stroke: 2px var(--ink);
    paint-order: stroke fill;
    letter-spacing: -0.02em;
    line-height: 1;
  }
  .lead-a { left: 0; top: 0; width: 495px; height: 100px; font-size: 72px; padding-left: 4px; }
  .lead-b { left: 0; top: 104px; width: 495px; height: 88px; font-size: 45px; padding-left: 4px; }
  .lead-nado {
    left: 500px; top: 0; width: 250px; height: 192px;
    font-size: 118px; justify-content: center;
  }
  .main { left: 8px; right: 8px; height: 136px; justify-content: center; }
  .main-1 { top: 202px; font-size: 134px; }
  .main-2 { top: 350px; font-size: 118px; }
  .main-3 { top: 498px; font-size: 110px; }
  .main-4 { top: 646px; font-size: 118px; }

  .pitch {
    position: absolute;
    left: 50px; top: 880px;
    width: 340px;
    transform: rotate(-17deg);
    transform-origin: 50% 50%;
    white-space: nowrap;
  }
  .pitch-lead {
    color: var(--rose);
    font-weight: 800;
    font-size: 24px;
    line-height: 1.3;
  }
  .pitch-close {
    margin-top: 10px;
    color: var(--ink);
    font-weight: 800;
    font-size: 24px;
    line-height: 1.15;
  }
  .pitch-close .qol {
    font-size: 64px;
    color: var(--sky);
    -webkit-text-stroke: 2px var(--ink);
    paint-order: stroke fill;
    font-weight: 900;
  }

  .byline { position: absolute; left: 505px; top: 800px; width: 240px; }
  .byline-tag { font-size: 10px; font-weight: 500; color: var(--ink); letter-spacing: 0.05em; padding-left: 6px; }
  .author { font-size: 40px; font-weight: 900; color: var(--ink); line-height: 1.1; padding-left: 6px; }
  .author small { font-size: 26px; }
  .topics {
    list-style: none;
    margin-top: 12px;
    text-align: center;
    color: var(--rose);
    font-weight: 800;
    font-size: 16px;
    line-height: 20px;
    white-space: nowrap;
  }
  .bonus {
    position: absolute; left: 470px; top: 1128px; width: 275px;
    text-align: right;
    color: var(--ink); font-size: 13px; font-weight: 800; line-height: 1.35;
  }
  .bonus span { display: block; font-size: 10px; font-weight: 500; }
</style>
</head>
<body>
<main class="cover">
  <h1 class="title">
    <span class="title-line lead-a">「5つの航路」</span>
    <span class="title-line lead-b">「ヴォルテノ大年譜」</span>
    <span class="title-line lead-nado">など</span>
    <span class="title-line main main-1">人類普遍の</span>
    <span class="title-line main main-2">必読真理書を</span>
    <span class="title-line main main-3">ギュっと1冊に</span>
    <span class="title-line main main-4">まとめました</span>
  </h1>

  <section class="pitch">
    <p class="pitch-lead">メンタルトレーナーが<br>視点で要点を抽出した<br>人類普遍のフレーム<br>ワーク読本。</p>
    <p class="pitch-close">この1冊があなたの<br><span class="qol">QOL</span>を<br>大きく変える!</p>
  </section>

  <section class="byline">
    <p class="byline-tag">mental trainer</p>
    <p class="author">RUNO<small>著</small></p>
    <ul class="topics">
      <li>5つの航路</li>
      <li>ベルモント心理学</li>
      <li>ハルヴェンの欲求5段階説</li>
      <li>シックスヒューマンニーズ</li>
      <li>ヴォルテノ大年譜</li>
      <li>人生フレームワーク</li>
    </ul>
  </section>

  <p class="bonus">これからも成長する成功分野32選<span>TALKOまとめ特典付き</span></p>
</main>
</body>
</html>
```